PELUNO soap beauty bar

I need a box designed to put a 4oz bar of soap inside. All sides of the box need design. A refreshingly fragrant blend of citrus and spicy notes, it is made with a blend of essential oils including ginger, mandarin, lemon and orange flowers

Target Market(s)

Homeless people

Requirements
Must have
• My company logo as pictured with text and design like a standard bar of soap. Weight 4oz, ingredients:
Olive oil, Coconut oil,Organic sustainable palm oil,Water,Lye,Shea butter, orange, ginger, mandarin, lemon essential oil. uploading pics for inspiration.
Nice to have
• The soap box measurements are Dimensions (L x W x H). 5.75 x 3.80 x 5.60 Inches ...

```html
<!DOCTYPE html>
<html lang="en">
<head>
<meta charset="utf-8">
<title>PELUNO Handmade Soap – Box Front</title>
<link rel="stylesheet" href="https://fonts.googleapis.com/css2?family=Jost:wght@400;500;700&family=Roboto+Condensed:wght@400&display=swap">
<style>
  :root {
    --page-bg: #ffffff;
    --panel-cream: #f4f3f1;
    --ink-dark: #231f1c;
    --brand-green: #2a9a3c;
    --brand-red: #d8262f;
    --leaf-green: #bcdba0;
    --leaf-green-soft: #c8e2b0;
    --label-fill: #f3f6ee;
    --label-text: #86b266;
    --weight-text: #2f6a2a;
  }
  * { margin: 0; padding: 0; box-sizing: border-box; }
  html, body {
    width: 1200px;
    height: 858px;
    overflow: hidden;
    background: var(--page-bg);
  }
  .canvas {
    position: relative;
    width: 1200px;
    height: 858px;
  }
  .box-front {
    position: absolute;
    left: 327px;
    top: 97px;
    width: 476px;
    height: 725px;
    background: var(--panel-cream);
    overflow: hidden;
  }
  .brand {
    position: absolute;
    top: 40px;
    left: 0;
    width: 100%;
    display: flex;
    flex-direction: column;
    align-items: center;
  }
  .brand-dot {
    width: 92px;
    height: 92px;
    border-radius: 50%;
    background: var(--brand-red);
  }
  .brand-name {
    margin-top: 24px;
    font-family: 'Jost', sans-serif;
    font-weight: 700;
    font-size: 46px;
    line-height: 1;
    letter-spacing: 1px;
    color: var(--brand-green);
  }
  .product-kind {
    position: absolute;
    top: 246px;
    width: 100%;
    text-align: center;
    font-family: 'Jost', sans-serif;
    font-weight: 400;
    font-size: 20px;
    line-height: 28px;
    letter-spacing: 6px;
    padding-left: 6px;
    color: var(--ink-dark);
  }
  .product-name {
    position: absolute;
    top: 270px;
    width: 100%;
    text-align: center;
    font-family: 'Jost', sans-serif;
    font-weight: 400;
    font-size: 100px;
    line-height: 1.2;
    letter-spacing: 10px;
    padding-left: 10px;
    color: var(--ink-dark);
  }
  .lower-band {
    position: absolute;
    left: 0;
    top: 407px;
    width: 100%;
    height: 318px;
    background: linear-gradient(180deg, var(--leaf-green-soft), var(--leaf-green));
  }
  .scent-label {
    position: absolute;
    left: 63px;
    top: 24px;
    width: 342px;
    height: 67px;
    border-radius: 16px;
    background: var(--label-fill);
    display: flex;
    align-items: center;
    justify-content: center;
    text-align: center;
    font-family: 'Roboto Condensed', sans-serif;
    font-size: 13px;
    line-height: 1.35;
    letter-spacing: 0.6px;
    color: var(--label-text);
    text-transform: uppercase;
  }
  .net-weight {
    position: absolute;
    top: 191px;
    width: 100%;
    text-align: center;
    font-family: 'Roboto Condensed', sans-serif;
    font-size: 18px;
    line-height: 24px;
    color: var(--weight-text);
  }
</style>
</head>
<body>
  <main class="canvas">
    <section class="box-front">
      <header class="brand">
        <span class="brand-dot" aria-hidden="true"></span>
        <span class="brand-name">PELUNO</span>
      </header>
      <p class="product-kind">HANDMADE</p>
      <h1 class="product-name">SOAP</h1>
      <div class="lower-band" role="img" aria-label="Soft green band with a faint pattern of leaves and flowers">
        <p class="scent-label">Refreshingly fragrant blend of citrus<br>and spicy notes, with ginger, mandarin,<br>lemon and orange flowers</p>
        <p class="net-weight">Net Weight 4oz</p>
      </div>
    </section>
  </main>
</body>
</html>
```